Business Card Design Project

We are a distribution company providing goods to Latin America. We sell everything from Medical equipment, generic medicines, to carecliners. The logo that we use is attached. The logo can incorporate different colors other than black for versatility. The company name is Valdren Global Enterprises and/or VGE. The card will be printed using 1 or more of the following: Silk mounted and/or embossed. So if the design ideas could be made to incorporate that technique or any other unique techniques, it would be great. The target market is dialysis centers/doctors.

Basic Info for card:
Marna Dowell
Purchasing Manager
417-305-6184 direct
417-521-7790 fax
marna.dowell@valdrenvge.example
www.valdrenvge.example

Target Market(s)

Latin America

Industry/Entity Type

Business

Requirements
Nice to have
• The Front of the card should have the basic contact information with company name/logo. The back of the card could incorporate

```html
<!DOCTYPE html>
<html lang="en">
<head>
<meta charset="utf-8">
<title>Valdren Global Enterprises – Business Card</title>
<link rel="stylesheet" href="https://fonts.googleapis.com/css2?family=Questrial&family=Cutive+Mono&display=swap">
<style>
  :root {
    --violet: #3b3580;
    --violet-back: #3f3179;
    --yellow: #f2e62a;
    --white: #ffffff;
    --ink: #111111;
    --grey: #6b6b6b;
    --page: #ffffff;
    --edge: #c9c6dd;
  }
  * { box-sizing: border-box; margin: 0; padding: 0; }
  html, body { width: 1200px; height: 329px; overflow: hidden; background: var(--page); }
  body { position: relative; font-family: "Questrial", "Century Gothic", sans-serif; }

  .card {
    position: absolute; top: 5px; width: 550px; height: 316px;
    border-radius: 11px; overflow: hidden;
  }
  .card--front { left: 5px; background: var(--violet); box-shadow: 0 0 0 1px var(--edge); }
  .card--back { left: 578px; background: var(--violet-back); }

  .front__url {
    position: absolute; right: 7px; top: 30px;
    color: var(--yellow); font-size: 15px;
  }
  .front__company {
    position: absolute; right: 6px; top: 62px;
    color: var(--white); font-size: 29px; letter-spacing: -0.5px; white-space: nowrap;
  }
  .accent { color: var(--yellow); }

  .front__band {
    position: absolute; left: 0; top: 129px; width: 100%; height: 103px;
    background: var(--white);
  }
  .front__mark {
    position: absolute; left: 32px; top: 34px; display: flex; align-items: center; gap: 8px;
    color: var(--ink); font-size: 30px;
  }
  .front__mark-dot { width: 22px; height: 22px; border-radius: 50%; background: var(--ink); }
  .front__name {
    position: absolute; left: 172px; top: 40px;
    color: var(--ink); font-size: 20px;
  }
  .front__title {
    position: absolute; left: 331px; top: 44px;
    font-family: "Cutive Mono", "Courier New", monospace; color: var(--grey); font-size: 15px;
  }

  .front__email {
    position: absolute; left: 0; width: 100%; top: 250px; text-align: center;
    color: var(--white); font-size: 18px;
  }
  .front__phone {
    position: absolute; top: 280px; display: flex; align-items: center; gap: 3px;
    font-family: "Cutive Mono", "Courier New", monospace; color: var(--yellow); font-size: 14px;
  }
  .front__phone--direct { left: 114px; }
  .front__phone--fax { left: 303px; }
  .front__phone svg { width: 19px; height: 19px; }

  .back__ghost {
    position: absolute; left: 50%; top: 134px; transform: translateX(-50%) scaleX(1.05);
    color: var(--white); opacity: 0.32; font-size: 38px; white-space: nowrap; letter-spacing: -1px;
  }
  .back__company {
    position: absolute; left: 0; width: 100%; top: 138px; text-align: center;
    color: var(--white); font-size: 30px; letter-spacing: -0.5px; white-space: nowrap;
  }
  .back__url {
    position: absolute; left: 0; width: 100%; top: 179px; text-align: center;
    color: var(--yellow); font-size: 15px;
  }
</style>
</head>
<body>
  <section class="card card--front">
    <p class="front__url">www.valdrenvge.example</p>
    <h1 class="front__company">VALDREN <span class="accent">GLOBAL</span> ENTERPRISES</h1>

    <div class="front__band">
      <div class="front__mark"><span class="front__mark-dot"></span>VGE</div>
      <p class="front__name">Marna Dowell</p>
      <p class="front__title">Purchasing Manager</p>
    </div>

    <p class="front__email">marna.dowell@valdrenvge.example</p>
    <p class="front__phone front__phone--direct">417-305-6184
      <svg viewBox="0 0 20 20" aria-label="direct line">
        <circle cx="10" cy="10" r="8.5" fill="none" stroke="var(--white)" stroke-width="1.4"/>
        <path d="M7 5.5l2 2-1 1.2c.6 1.3 1.6 2.3 2.9 2.9l1.2-1 2 2-1.2 1.4c-3.4-.4-6.3-3.3-6.7-6.7z" fill="var(--yellow)"/>
      </svg>
    </p>
    <p class="front__phone front__phone--fax">417-521-7790
      <svg viewBox="0 0 20 20" aria-label="fax">
        <circle cx="10" cy="10" r="8.5" fill="none" stroke="var(--white)" stroke-width="1.4"/>
        <rect x="6" y="5" width="8" height="4" fill="none" stroke="var(--yellow)" stroke-width="1.2"/>
        <rect x="5" y="9" width="10" height="6" fill="var(--yellow)"/>
      </svg>
    </p>
  </section>

  <section class="card card--back">
    <p class="back__ghost" aria-hidden="true">VALDREN GLOBAL ENTERPRISES</p>
    <h2 class="back__company">VALDREN <span class="accent">GLOBAL</span> ENTERPRISES</h2>
    <p class="back__url">www.valdrenvge.example</p>
  </section>
</body>
</html>
```